I need a DVD cover for a training package contained on a disc. There are four modules within the resource so I need these to be visible on the cover. They are:
Cultural Competence Healthcare Provision
Provision of Care to CALD Women having Babies in Australia
Cultural Considerations in Aged Care Provision
Cultural Competence in Mental Health

I have attached a cd cover with an image of a waratah. This is Bellmore Ridge Valley Health's logo so needs to appear on the front cover also.
The smaller logo with the waratah also needs to be on the front cover. Please note these are the only copies I could obtain so if the quality is too poor you may need to reproduce.

The following should appear on the back cover:
‘Pathways to Inclusive Patient Support’ is a collaborative achievement of the Multicultural Health Liaison Officers in Acute Care, Obstetrics, Aged Care and Mental Health under the guidance of the Director, Multicultural Health Service in Bellmore Ridge Valley Local Health District. Staff members from the specialist teams and community members graciously contributed to the production of podcasts and video clips.
Photography, video clips and technical support was provided by Daniel Follett - E-learning Developer and Designer - Lumen Tutors.
This project was coordinated by Colleen Bastow, Multicultural Health Liaison Officer (Acute Care, Lower Brindlewood Coastal Hospital Network).

```html
<!DOCTYPE html>
<html lang="en">
<head>
<meta charset="utf-8">
<title>Pathways to Inclusive Patient Support – DVD Cover</title>
<link rel="stylesheet" href="https://fonts.googleapis.com/css2?family=Tinos:wght@400;700&family=Arimo:wght@400;700&display=swap">
<style>
  :root {
    --cover-blue: #0b4f9f;
    --panel-blue: #0d56aa;
    --edge-blue: #1d67bb;
    --sky-light: #b9e2f7;
    --sky-mid: #5ea9dc;
    --white: #ffffff;
    --ink: #1f3f77;
    --accent-red: #d7193f;
  }
  * { margin: 0; padding: 0; box-sizing: border-box; }
  html, body { width: 1200px; height: 802px; overflow: hidden; background: var(--white); }
  .dvd-cover {
    position: relative; width: 1200px; height: 802px;
    background: var(--cover-blue); overflow: hidden;
    font-family: "Tinos", "Times New Roman", serif; color: var(--white);
  }

  /* Back cover */
  .back-cover { position: absolute; left: 0; top: 0; width: 588px; height: 802px; }
  .photo-grid {
    position: absolute; left: 32px; top: 30px;
    display: grid; grid-template-columns: repeat(4, 118px); grid-auto-rows: 124px;
    column-gap: 6px; row-gap: 10px;
  }
  .photo-grid span { background: var(--white); }
  .back-title { position: absolute; left: 32px; top: 318px; font-size: 25px; font-weight: 700; }
  .back-copy {
    position: absolute; left: 32px; top: 357px; width: 525px;
    font-size: 15.5px; font-weight: 700; line-height: 18.6px;
  }
  .back-copy p + p { margin-top: 18px; }

  /* Spine */
  .spine {
    position: absolute; left: 588px; top: 0; width: 30px; height: 802px;
    background: var(--cover-blue);
  }
  .spine-title {
    position: absolute; left: 1px; top: 70px; width: 28px; height: 420px;
    writing-mode: vertical-rl; font-size: 22px; font-weight: 700; white-space: nowrap;
  }
  .spine-badge {
    position: absolute; left: 0; top: 490px; width: 30px; height: 312px; background: var(--white);
  }
  .spine-badge span {
    position: absolute; left: 7px; top: 28px; writing-mode: vertical-rl;
    font-size: 9px; font-weight: 700; color: var(--ink); font-family: "Arimo", Arial, sans-serif;
  }

  /* Front cover */
  .front-cover { position: absolute; left: 618px; top: 0; width: 582px; height: 802px; }
  .photo-band {
    position: absolute; left: 2px; top: 12px; width: 580px; height: 195px;
    background: var(--panel-blue); border-top: 2px solid var(--edge-blue);
  }
  .photo {
    position: absolute; top: 58px; height: 118px;
    background: linear-gradient(160deg, #e7ecef 0%, #c9b9a5 55%, #8c95a6 100%);
  }
  .photo--family { left: 16px; width: 142px; }
  .photo--newborn { left: 165px; width: 126px; background: linear-gradient(160deg, #f3efe9, #d9b8a0 60%, #a99c92); }
  .photo--aged-care { left: 298px; width: 126px; background: linear-gradient(160deg, #f1f3f4, #c4c6c9 55%, #7d8aa0); }
  .photo--senior { left: 430px; width: 126px; background: linear-gradient(160deg, #eef2f6, #b5c6d9 55%, #6a86ad); }

  .title-panel {
    position: absolute; left: 2px; top: 208px; width: 580px; height: 594px;
    border-top: 3px solid var(--edge-blue);
    background: linear-gradient(180deg, var(--panel-blue) 0%, var(--panel-blue) 30%, #3f8ccf 60%, #2a6fba 100%);
  }
  .medical-backdrop {
    position: absolute; left: 0; top: 170px; width: 580px; height: 424px;
    background: radial-gradient(ellipse 380px 240px at 330px 250px, var(--sky-light) 0%, var(--sky-mid) 45%, rgba(13,86,170,0) 100%);
  }
  .front-title { position: absolute; left: 12px; top: 12px; font-size: 44px; font-weight: 700; line-height: 57px; }
  .module-list {
    position: absolute; left: 10px; top: 199px; list-style: none;
    font-size: 20.5px; font-weight: 700; line-height: 24.5px; white-space: nowrap;
    text-shadow: 1px 1px 2px rgba(0,0,0,.55);
  }

  /* Organisation bars */
  .org-bar {
    position: absolute; background: var(--white); height: 44px;
    display: flex; align-items: center; gap: 10px; padding-left: 22px;
    font-family: "Arimo", Arial, sans-serif; font-weight: 700; font-size: 12.5px;
    color: var(--ink); line-height: 14px;
  }
  .org-bar::before { content: ""; width: 18px; height: 18px; background: var(--accent-red); flex: none; }
  .org-bar--back { left: 248px; top: 670px; width: 334px; }
  .org-bar--front { left: 832px; top: 668px; width: 368px; }
</style>
</head>
<body>
<main class="dvd-cover">

  <section class="back-cover">
    <div class="photo-grid">
      <span></span><span></span><span></span><span></span>
      <span></span><span></span><span></span><span></span>
    </div>
    <h2 class="back-title">Pathways to Inclusive Patient Support</h2>
    <div class="back-copy">
      <p>is a collaborative achievement of the Multicultural Health Liaison Officers in Acute Care, Obstetrics, Aged Care and Mental Health under the guidance of the Director, Multicultural Health Service in Bellmore Ridge Valley Local Health District. Staff members from the specialist teams and community members graciously contributed to the production of podcasts and video clips.</p>
      <p>Photography, video clips and technical support was provided by Daniel Follett - E-learning Developer and Designer - Lumen Tutors.<br>
      This project was coordinated by Colleen Bastow, Multicultural Health Liaison Officer (Acute Care, Lower Brindlewood Coastal Hospital Network).</p>
    </div>
  </section>
  <div class="org-bar org-bar--back">Bellmore Ridge Valley<br>Local Health District</div>

  <aside class="spine">
    <div class="spine-title">Pathways to Inclusive Patient Support</div>
    <div class="spine-badge"><span>Bellmore Ridge Valley Health</span></div>
  </aside>

  <section class="front-cover">
    <div class="photo-band">
      <div class="photo photo--family" role="img" aria-label="Photo of a multi-generational family smiling together"></div>
      <div class="photo photo--newborn" role="img" aria-label="Photo of parents holding a newborn baby"></div>
      <div class="photo photo--aged-care" role="img" aria-label="Photo of a nurse caring for an elderly woman"></div>
      <div class="photo photo--senior" role="img" aria-label="Photo of a smiling senior man"></div>
    </div>

    <div class="title-panel">
      <div class="medical-backdrop" role="img" aria-label="Background illustration of a heartbeat trace and medical cross on a glowing blue field"></div>
      <h1 class="front-title">Pathways<br>to Inclusive<br>Patient Support</h1>
      <ul class="module-list">
        <li>Cultural Competence Healthcare Provision</li>
        <li>Provision of Care to CALD Women having Babies in Australia</li>
        <li>Cultural Considerations in Aged Care Provision</li>
        <li>Cultural Competence in Mental Health</li>
      </ul>
    </div>
  </section>
  <div class="org-bar org-bar--front">Bellmore Ridge Valley<br>Local Health District</div>

</main>
</body>
</html>
```